Tolliver Partners
Business Cards, Letterhead, Envelope and 3-4 basic Power Point Slides
Tolliver Partners -
Creative Brief
Please submit designs for: Business Cards, Letterhead, No. 10 Envelope and 3-4 Basic Power Point Slides Please see our web site for more information: TolliverPartners.com
Corporate and Investor Services
We have already completed our logo and its is available for downloading. Please do not make changes to the logo.

```html
<!DOCTYPE html>
<html lang="en">
<head>
<meta charset="utf-8">
<title>Tolliver Partners – Stationery and Slides</title>
<link rel="stylesheet" href="https://fonts.googleapis.com/css2?family=Open+Sans:wght@400;700&display=swap">
<style>
:root{
  --green:#3f9b2c;
  --green-light:#8bcf4a;
  --green-dark:#1f6e1a;
  --blue:#2f6fb3;
  --ink:#444;
  --grey:#8a8a8a;
  --faint:#e6e6e6;
  --paper:#ffffff;
  --bg:#ffffff;
}
*{box-sizing:border-box;margin:0;padding:0}
html,body{width:1200px;height:626px;overflow:hidden;background:var(--bg)}
body{position:relative;font-family:"Open Sans",Arial,sans-serif;color:var(--ink)}
.label{position:absolute;font-size:8px;color:var(--grey);white-space:nowrap}
.sheet{position:absolute;background:var(--paper);box-shadow:0 1px 4px rgba(0,0,0,.22);overflow:hidden}
.wave{position:absolute;left:0;bottom:0;width:100%}
.brand{display:flex;align-items:center;gap:5px;font-weight:700;color:var(--green);white-space:nowrap;line-height:1}
.brand .dot{border-radius:50%;background:var(--green);flex:none}
.small-text{font-size:5px;line-height:1.5;color:var(--ink)}
.on-green{position:absolute;z-index:2;color:#fff}
.url{position:absolute;left:0;width:100%;text-align:center;font-size:6px;color:#fff;z-index:2}
.watermark{position:absolute;left:0;width:100%;display:flex;justify-content:center;align-items:center;gap:10px;font-weight:700;color:var(--faint);white-space:nowrap}
.watermark .dot{border-radius:50%;background:var(--faint)}
.slide2-band{position:absolute;left:0;top:0;width:100%;height:34px;background:linear-gradient(90deg,#ffffff 0%,#d7e6f4 40%,var(--blue) 100%)}
.map{position:absolute;right:8px;top:3px;width:120px;height:28px;background:radial-gradient(ellipse at center,rgba(31,76,135,.55),rgba(31,76,135,0) 70%)}
.placeholder{position:absolute;left:16px;width:100px;height:66px;border-radius:6px;background:linear-gradient(#f3f3f3,#dcdcdc);border:1px solid #cfcfcf}
.subtitle{font-size:8px;font-weight:700;color:#333;margin-bottom:6px}
.window{position:absolute;left:22px;bottom:34px;width:72px;height:30px;border:1px solid #c8c8c8;border-radius:2px;background:#fafafa}
</style>
</head>
<body>

<svg width="0" height="0" style="position:absolute">
  <defs>
    <linearGradient id="greenFill" x1="0" y1="0" x2="0" y2="1">
      <stop offset="0" stop-color="#9ad75a"/>
      <stop offset="0.5" stop-color="#4faa30"/>
      <stop offset="1" stop-color="#1f6e1a"/>
    </linearGradient>
    <symbol id="wave" viewBox="0 0 100 40" preserveAspectRatio="none">
      <path d="M0 22 Q50 46 100 10 L100 40 L0 40Z" fill="url(#greenFill)"/>
      <path d="M0 17 Q50 40 100 4" fill="none" stroke="#2f6fb3" stroke-width="1.2" vector-effect="non-scaling-stroke"/>
    </symbol>
  </defs>
</svg>

<!-- Business cards -->
<div class="label" style="left:40px;top:66px">Business Card</div>

<div class="sheet card-front" style="left:10px;top:91px;width:206px;height:120px">
  <div class="brand" style="position:absolute;left:10px;top:12px;font-size:7px"><span class="dot" style="width:14px;height:14px"></span>Tolliver Partners</div>
  <div class="small-text" style="position:absolute;left:29px;top:29px">1200 Market Street<br>Suite 400, Denver CO 80202</div>
  <svg class="wave" height="80"><use href="#wave"/></svg>
  <div class="small-text on-green" style="right:10px;bottom:6px;text-align:right;color:#fff">
    <b style="font-size:6px">Jordan Ellis</b><br>Managing Partner<br>T 555 014 2200
  </div>
</div>

<div class="sheet card-back" style="left:10px;top:221px;width:206px;height:115px">
  <div class="brand" style="position:absolute;left:14px;top:30px;font-size:14px"><span class="dot" style="width:20px;height:20px"></span>Tolliver Partners</div>
  <svg class="wave" height="50"><use href="#wave"/></svg>
  <div class="url" style="bottom:5px;text-align:right;padding-right:10px">TolliverPartners.com</div>
</div>

<!-- Envelope -->
<div class="sheet envelope" style="left:10px;top:379px;width:273px;height:199px">
  <div class="brand" style="position:absolute;left:14px;top:14px;font-size:8px"><span class="dot" style="width:16px;height:16px"></span>Tolliver Partners</div>
  <div class="small-text" style="position:absolute;left:35px;top:33px">1200 Market Street<br>Denver CO 80202</div>
  <div class="window"></div>
  <svg class="wave" height="110"><use href="#wave"/></svg>
</div>
<div class="label" style="left:130px;top:592px">Envelope</div>

<!-- Letterhead landscape -->
<div class="label" style="left:380px;top:28px">Letterhead A4 (Landscape)</div>
<div class="sheet letterhead-landscape" style="left:252px;top:48px;width:336px;height:348px">
  <div class="brand" style="position:absolute;left:30px;top:16px;font-size:7px"><span class="dot" style="width:22px;height:22px"></span>Tolliver Partners</div>
  <div class="small-text" style="position:absolute;left:57px;top:41px">1200 Market Street, Suite 400<br>Denver CO 80202 · T 555 014 2200</div>
  <div class="watermark" style="top:150px;font-size:30px"><span class="dot" style="width:36px;height:36px"></span>Tolliver Partners</div>
  <svg class="wave" height="70"><use href="#wave"/></svg>
</div>

<!-- Letterhead portrait -->
<div class="sheet letterhead-portrait" style="left:422px;top:72px;width:351px;height:514px">
  <div class="brand" style="position:absolute;left:22px;top:20px;font-size:9px"><span class="dot" style="width:22px;height:22px"></span>Tolliver Partners</div>
  <div class="small-text" style="position:absolute;left:22px;top:48px">1200 Market Street, Suite 400<br>Denver CO 80202 · T 555 014 2200</div>
  <div class="watermark" style="top:255px;font-size:30px"><span class="dot" style="width:36px;height:36px"></span>Tolliver Partners</div>
  <svg class="wave" height="80"><use href="#wave"/></svg>
  <div class="url" style="bottom:6px">TolliverPartners.com</div>
</div>
<div class="label" style="left:545px;top:603px">Letterhead A4 (Landscape)</div>

<!-- Slide 1 -->
<div class="label" style="left:1000px;top:15px">Powerpoint Slide 1</div>
<div class="sheet slide-title" style="left:811px;top:31px;width:377px;height:305px">
  <div class="brand" style="position:absolute;left:0;width:100%;top:120px;justify-content:center;font-size:30px;gap:10px"><span class="dot" style="width:34px;height:34px"></span>Tolliver Partners</div>
  <svg class="wave" height="90"><use href="#wave"/></svg>
  <div class="url" style="bottom:8px">TolliverPartners.com</div>
</div>

<!-- Slide 2 -->
<div class="sheet slide-content" style="left:811px;top:360px;width:377px;height:228px">
  <div class="slide2-band"><div class="map" role="img" aria-label="World map backdrop"></div></div>
  <div class="placeholder" style="top:44px" role="img" aria-label="Image placeholder"></div>
  <div class="placeholder" style="top:118px" role="img" aria-label="Image placeholder"></div>
  <div style="position:absolute;left:132px;top:44px;width:225px">
    <div class="subtitle">SUBTITLE HERE</div>
    <p class="small-text" style="margin-bottom:6px">Lorem ipsum dolor sit amet, consectetur adipiscing elit. Vestibulum ante ipsum primis in faucibus orci luctus et ultrices posuere cubilia curae. Donec velit neque, auctor sit amet aliquam vel, ullamcorper sit amet ligula.</p>
    <p class="small-text">Lorem ipsum dolor sit amet, consectetur adipiscing elit. Vestibulum ante ipsum primis in faucibus orci luctus et ultrices posuere cubilia curae. Donec velit neque, auctor sit amet aliquam vel, ullamcorper sit amet ligula.</p>
  </div>
  <svg class="wave" height="52"><use href="#wave"/></svg>
  <div class="url" style="bottom:3px">TolliverPartners.com</div>
</div>
<div class="label" style="left:1000px;top:603px">Powerpoint Slide 2</div>

</body>
</html>
```